Wedding Guestbook/Questionnaire Pages

I am looking for questionnaire-style guest book pages for a friend's wedding. The bride wants her guests to fill out a page of reflections on the couple and the wedding in lieu of a traditional guest book. The pages would be printed on 12x12 paper and bound in a book after the wedding.

I've attached a photo of the style of the pages as well as several documents that show colors and give a feel for the wedding.

I understand that this isn't a common project so I welcome any questions and would be more than happy to clarify things.

Thank you!

Target Market(s)

The bride and groom are a young couple and the wedding is more fun and whimisical than formal. The colors are primarily purple with green and silver accents.

Industry/Entity Type

Wedding

Requirements
Must have
• I would like to have 2 pages that are similar, but have different questions on them so that every guest doesn't answer the same questions. On each page it needs to say 'Mara & Declan,' 'May 27th, 2011,' and a place that says 'Guest Names' for the guest sign their names.
Nice to have
• Some of the questions we like are:
Do you have any advice or wishes for the bride and groom?
How far did you travel to get here?
How do you know Mara and Declan?
What’s your favorite memory with the bride and groom?
What has been your favorite part of the wedding?
What do you think they'll name their children?
Should not have
• The pages do not need to be extremely colorful. An ivory or white background with accents of color would be preferred.

```html
<!DOCTYPE html>
<html lang="en">
<head>
<meta charset="utf-8">
<title>Mara &amp; Declan – Guestbook Pages</title>
<link rel="stylesheet" href="https://fonts.googleapis.com/css2?family=Kaushan+Script&family=Satisfy&family=Dancing+Script:wght@400&display=swap">
<style>
  :root {
    --paper: #ffffff;
    --frame: #3a3a3a;
    --plum: #523f6b;
    --ink: #4d3a68;
    --leaf: #8fcf4c;
    --leaf-soft: #d9f0c2;
    --petal-light: #fbf2d8;
    --petal-pink: #e9b3d0;
    --petal-lilac: #a58fcf;
    --script: "Satisfy", "Dancing Script", "Kaushan Script", cursive;
  }
  * { box-sizing: border-box; margin: 0; padding: 0; }
  html, body {
    width: 1200px; height: 900px; overflow: hidden;
    background: var(--paper);
  }
  .spread { position: relative; width: 1200px; height: 900px; }
  .page {
    position: absolute; top: 138px; width: 597px; height: 598px;
    border: 2px solid var(--frame); background: var(--paper);
    font-family: var(--script); color: var(--ink);
  }
  .page--one { left: 3px; }
  .page--two { left: 603px; }
  .page > * { position: absolute; }

  .nameplate {
    left: 160px; top: 19px; width: 277px; height: 103px;
    background: var(--plum); border-radius: 24px;
  }
  .couple {
    left: 186px; top: 48px; width: 240px; text-align: center;
    font-family: "Kaushan Script", cursive; font-weight: 400;
    font-size: 36px; line-height: 1; letter-spacing: -0.5px;
    color: #fff; white-space: nowrap;
  }
  .date {
    left: 318px; top: 103px; font-size: 11px; line-height: 14px; color: #fff;
    white-space: nowrap;
  }
  .bloom {
    border-radius: 50%;
    background: radial-gradient(circle, var(--petal-lilac) 0 10%, var(--petal-light) 18%, var(--petal-pink) 55%, var(--petal-lilac) 80%, transparent 82%);
  }
  .swirl {
    border-radius: 40px;
    background: radial-gradient(ellipse, var(--leaf-soft) 0%, rgba(217,240,194,0.4) 60%, transparent 72%);
  }
  .bloom--crown-left { left: 121px; top: 9px; width: 60px; height: 56px; }
  .bloom--crown-right { left: 410px; top: 86px; width: 60px; height: 56px; }
  .swirl--crown-left { left: 37px; top: 37px; width: 125px; height: 70px; }
  .swirl--crown-right { left: 442px; top: 37px; width: 127px; height: 70px; }

  .signature-rule {
    left: 160px; top: 164px; width: 279px; height: 3px; background: var(--leaf);
  }
  .signature-label {
    left: 192px; top: 168px; width: 120px; text-align: center; font-size: 18px; line-height: 22px;
  }

  .question { font-size: 18px; line-height: 20px; white-space: nowrap; }
  .center { text-align: center; }
  .right { text-align: right; }
  .answer-line { height: 3px; background: var(--ink); }
</style>
</head>
<body>
<main class="spread">

  <section class="page page--one">
    <div class="swirl swirl--crown-left" role="img" aria-label="Green swirl ornament"></div>
    <div class="swirl swirl--crown-right" role="img" aria-label="Green swirl ornament"></div>
    <div class="nameplate"></div>
    <h1 class="couple">Mara &amp; Declan</h1>
    <p class="date">May 27th, 2011</p>
    <div class="bloom bloom--crown-left" role="img" aria-label="Pink and lilac flower"></div>
    <div class="bloom bloom--crown-right" role="img" aria-label="Pink and lilac flower"></div>
    <div class="signature-rule"></div>
    <p class="signature-label">guest names</p>

    <div class="bloom" style="left:25px;top:188px;width:58px;height:54px" role="img" aria-label="Pink and lilac flower"></div>
    <p class="question center" style="left:80px;top:192px;width:150px">How do you know<br>Mara &amp; Declan?</p>
    <div class="answer-line" style="left:39px;top:245px;width:178px"></div>
    <div class="answer-line" style="left:39px;top:273px;width:178px"></div>
    <div class="answer-line" style="left:39px;top:301px;width:178px"></div>
    <div class="answer-line" style="left:39px;top:329px;width:178px"></div>
    <div class="answer-line" style="left:39px;top:357px;width:178px"></div>
    <div class="answer-line" style="left:39px;top:385px;width:178px"></div>

    <p class="question center" style="left:255px;top:205px;width:322px">What advice or wishes do you have<br>for the bride &amp; groom?</p>
    <div class="answer-line" style="left:255px;top:271px;width:322px"></div>
    <div class="answer-line" style="left:255px;top:294px;width:322px"></div>
    <div class="answer-line" style="left:255px;top:318px;width:322px"></div>
    <div class="answer-line" style="left:255px;top:342px;width:322px"></div>
    <div class="answer-line" style="left:255px;top:365px;width:322px"></div>
    <div class="answer-line" style="left:255px;top:388px;width:322px"></div>

    <p class="question" style="left:35px;top:412px;width:215px">Where do you think Mara<br>&amp; Declan will live?</p>
    <div class="bloom" style="left:183px;top:447px;width:46px;height:42px" role="img" aria-label="Pink and lilac flower"></div>
    <div class="answer-line" style="left:37px;top:472px;width:148px"></div>
    <div class="answer-line" style="left:37px;top:500px;width:178px"></div>
    <div class="answer-line" style="left:37px;top:528px;width:178px"></div>
    <div class="answer-line" style="left:37px;top:556px;width:178px"></div>

    <p class="question" style="left:261px;top:418px;width:155px">What has been your<br>favorite part of<br>the wedding?</p>
    <div class="answer-line" style="left:415px;top:442px;width:154px"></div>
    <div class="answer-line" style="left:365px;top:466px;width:204px"></div>
    <div class="answer-line" style="left:263px;top:491px;width:306px"></div>
    <div class="answer-line" style="left:263px;top:516px;width:306px"></div>

    <div class="swirl" style="left:315px;top:530px;width:202px;height:54px" role="img" aria-label="Green swirl ornament with a pink and lilac flower"></div>
  </section>

  <section class="page page--two">
    <div class="swirl swirl--crown-left" role="img" aria-label="Green swirl ornament"></div>
    <div class="swirl swirl--crown-right" role="img" aria-label="Green swirl ornament"></div>
    <div class="nameplate"></div>
    <h1 class="couple">Mara &amp; Declan</h1>
    <p class="date">May 27th, 2011</p>
    <div class="bloom bloom--crown-left" role="img" aria-label="Pink and lilac flower"></div>
    <div class="bloom bloom--crown-right" role="img" aria-label="Pink and lilac flower"></div>
    <div class="signature-rule"></div>
    <p class="signature-label">guest names</p>

    <p class="question" style="left:35px;top:197px;width:160px">What do you think<br>Mara &amp; Declan will<br>name their<br>children?</p>
    <div class="answer-line" style="left:197px;top:217px;width:152px"></div>
    <div class="answer-line" style="left:137px;top:242px;width:212px"></div>
    <div class="answer-line" style="left:112px;top:267px;width:237px"></div>
    <div class="answer-line" style="left:33px;top:292px;width:316px"></div>
    <div class="answer-line" style="left:33px;top:317px;width:316px"></div>

    <p class="question" style="left:382px;top:183px;width:135px">How far did you<br>travel to be here?</p>
    <div class="bloom" style="left:512px;top:180px;width:56px;height:52px" role="img" aria-label="Pink and lilac flower"></div>
    <div class="answer-line" style="left:382px;top:241px;width:183px"></div>
    <div class="answer-line" style="left:382px;top:267px;width:183px"></div>
    <div class="answer-line" style="left:382px;top:292px;width:183px"></div>
    <div class="answer-line" style="left:382px;top:317px;width:183px"></div>

    <div class="swirl" style="left:87px;top:322px;width:205px;height:52px" role="img" aria-label="Green swirl ornament with a pink and lilac flower"></div>
    <p class="question center" style="left:35px;top:373px;width:322px">Share your favorite memory with<br>the bride &amp; groom.</p>
    <div class="answer-line" style="left:35px;top:439px;width:322px"></div>
    <div class="answer-line" style="left:35px;top:462px;width:322px"></div>
    <div class="answer-line" style="left:35px;top:486px;width:322px"></div>
    <div class="answer-line" style="left:35px;top:509px;width:322px"></div>
    <div class="answer-line" style="left:35px;top:533px;width:322px"></div>
    <div class="answer-line" style="left:35px;top:556px;width:322px"></div>

    <p class="question right" style="left:362px;top:346px;width:205px">Did anything interesting<br>happen today that we<br>may have missed?</p>
    <div class="bloom" style="left:377px;top:392px;width:46px;height:46px" role="img" aria-label="Pink and lilac flower"></div>
    <div class="answer-line" style="left:427px;top:436px;width:140px"></div>
    <div class="answer-line" style="left:387px;top:461px;width:183px"></div>
    <div class="answer-line" style="left:387px;top:485px;width:183px"></div>
    <div class="answer-line" style="left:387px;top:509px;width:183px"></div>
    <div class="answer-line" style="left:387px;top:533px;width:183px"></div>
    <div class="answer-line" style="left:387px;top:557px;width:183px"></div>
  </section>

</main>
</body>
</html>
```